One page financial canvas needed

I am in the process of developing a financial planning process that uses a one page canvas as a tool for financial education and to explain simple and complex financial strategies to clients. I have the layout and content sorted, just need a hand making it look professional.

It should be a fairly simple project and i have attached a very rough hand drawn canvas showing the desired layout and content. Please feel free to be creative with the design keeping in mind this layout has been chosen to achieve certain outcomes.

Target Market(s)

25-45 Year old Homeowners who are interested in taking better care of the finances

Industry/Entity Type

Financial

Colors

Designer to choose colors to be used in the design.

Requirements
Must have
• very close to the layout in the attached file

```html
<!DOCTYPE html>
<html lang="en">
<head>
<meta charset="utf-8">
<title>Financial Planning Canvas</title>
<link href="https://fonts.googleapis.com/css2?family=Ubuntu:wght@400&display=swap" rel="stylesheet">
<style>
  :root {
    --page-bg: #ececec;
    --panel-blue: #2468a8;
    --panel-blue-light: #4b95d1;
    --centre-bg: #ededed;
    --rule: #333333;
    --pill-top: #7d8ee0;
    --pill-mid: #4a5ec4;
    --pill-bottom: #2e3f9e;
    --pill-edge: #ffffff;
    --band: #bfc5dc;
    --text-light: #ffffff;
  }
  * { box-sizing: border-box; margin: 0; padding: 0; }
  html, body { width: 1200px; height: 858px; overflow: hidden; }
  body { background: var(--page-bg); font-family: "Ubuntu", sans-serif; }

  .planner { position: absolute; left: 10px; top: 12px; width: 1180px; height: 834px; overflow: hidden; }

  .side-panel { position: absolute; top: 0; height: 758px; background: linear-gradient(90deg, var(--panel-blue-light) 0%, var(--panel-blue) 35%, var(--panel-blue) 100%); }
  .side-panel--left { left: 0; width: 301px; }
  .side-panel--right { left: 879px; width: 301px; background: linear-gradient(90deg, var(--panel-blue) 0%, var(--panel-blue) 80%, #3a82c4 100%); }

  .cash-area { position: absolute; left: 301px; top: 0; width: 578px; height: 758px; background: var(--centre-bg); }

  .time-band { position: absolute; left: 0; top: 758px; width: 1180px; height: 76px; background: var(--band); }

  .rule { position: absolute; background: var(--rule); }
  .rule--v { width: 1.5px; left: 590px; }
  .rule--h { height: 1.5px; top: 379px; }

  .photo { position: absolute; border: 3px solid #f4f4f4; border-radius: 2px; box-shadow: 0 1px 3px rgba(0,0,0,.35); }
  .photo--goals { left: 10px; top: 11px; width: 145px; height: 120px; background: linear-gradient(160deg, #c9c96a, #5a6e6a 60%, #3f8f5a); }
  .photo--income { left: 379px; top: 11px; width: 140px; height: 86px; background: radial-gradient(circle at 50% 45%, #a9ad8a, #e9e9dc 55%, #ffffff); }
  .photo--expenses { left: 661px; top: 11px; width: 143px; height: 86px; background: linear-gradient(135deg, #e3ded6, #f3f3f3 50%, #8ab0d8); }
  .photo--assets { left: 339px; top: 390px; width: 140px; height: 82px; background: linear-gradient(180deg, #6fa3d6 0%, #dfe5ea 45%, #c7c2b4 75%, #5b7a3f 100%); }
  .photo--debt { left: 705px; top: 390px; width: 139px; height: 82px; background: linear-gradient(135deg, #9a6a44, #d9b98a 55%, #c84870); }
  .photo--fears { left: 893px; top: 11px; width: 142px; height: 87px; background: radial-gradient(circle at 55% 50%, #8a5a44, #2c1a14 70%); }
  .photo--frustrations { left: 893px; top: 266px; width: 142px; height: 87px; background: linear-gradient(90deg, #d8dbe0, #c9a682 55%, #eceae6); }
  .photo--partners { left: 893px; top: 520px; width: 142px; height: 86px; background: radial-gradient(circle, #c98a66, #e8d8cc 60%, #f4f0ee); }

  .money-burst { position: absolute; left: 507px; top: 291px; width: 166px; height: 166px; border-radius: 50%;
    background: radial-gradient(circle, #c9d2b5 0%, #8f9c74 45%, #c3c9ad 80%, rgba(195,201,173,0) 100%); }

  .wealth { position: absolute; left: 486px; top: 654px; width: 208px; height: 104px; border-radius: 104px 104px 0 0;
    background: radial-gradient(circle at 50% 100%, #f0b02a, #c46a12 60%, #6b2a08); }
  .wealth__label { position: absolute; left: 0; right: 0; top: 56px; text-align: center; color: var(--text-light); font-size: 34px; line-height: 1; letter-spacing: -0.5px; }

  .pill { position: absolute; display: flex; align-items: center; justify-content: center;
    color: var(--text-light); font-size: 35px; line-height: 1; letter-spacing: -0.5px; white-space: nowrap;
    border: 2px solid var(--pill-edge); border-radius: 24px;
    background: linear-gradient(180deg, var(--pill-top) 0%, var(--pill-mid) 45%, var(--pill-bottom) 100%);
    box-shadow: 0 2px 3px rgba(0,0,0,.4); }
  .pill--goals { left: 10px; top: 144px; width: 133px; height: 43px; }
  .pill--income { left: 341px; top: 110px; width: 216px; height: 46px; }
  .pill--expenses { left: 625px; top: 110px; width: 215px; height: 46px; }
  .pill--cashflow { left: 452px; top: 234px; width: 275px; height: 47px; }
  .pill--assets { left: 325px; top: 486px; width: 169px; height: 46px; }
  .pill--debt { left: 689px; top: 486px; width: 169px; height: 46px; }
  .pill--fears { left: 893px; top: 108px; width: 129px; height: 47px; }
  .pill--frustrations { left: 893px; top: 365px; width: 273px; height: 45px; }
  .pill--partners { left: 893px; top: 620px; width: 191px; height: 47px; }
  .pill--time { left: 94px; top: 768px; width: 107px; height: 48px; }

  .clock { position: absolute; left: 24px; top: 765px; width: 56px; height: 56px; }
</style>
</head>
<body>
  <main class="planner">
    <section class="side-panel side-panel--left"></section>
    <section class="cash-area"></section>
    <section class="side-panel side-panel--right"></section>
    <footer class="time-band"></footer>

    <div class="rule rule--v" style="top:35px;height:192px"></div>
    <div class="rule rule--v" style="top:468px;height:177px"></div>
    <div class="rule rule--h" style="left:313px;width:188px"></div>
    <div class="rule rule--h" style="left:680px;width:188px"></div>

    <div class="photo photo--goals" role="img" aria-label="Photo of a person placing sticky notes on a board"></div>
    <div class="pill pill--goals">GOALS</div>

    <div class="photo photo--income" role="img" aria-label="Photo of a roll of banknotes"></div>
    <div class="pill pill--income">INCOME</div>

    <div class="photo photo--expenses" role="img" aria-label="Photo of a hand writing beside a calculator and chart"></div>
    <div class="pill pill--expenses">EXPENSES</div>

    <div class="pill pill--cashflow">CASH FLOW</div>
    <div class="money-burst" role="img" aria-label="Circular fan of banknotes"></div>

    <div class="photo photo--assets" role="img" aria-label="Photo of a two-storey family house"></div>
    <div class="pill pill--assets">ASSETS</div>

    <div class="photo photo--debt" role="img" aria-label="Photo of urgent final notice bills"></div>
    <div class="pill pill--debt">DEBT</div>

    <div class="wealth" role="img" aria-label="Gold bars and coins">
      <span class="wealth__label">WEALTH</span>
    </div>

    <div class="photo photo--fears" role="img" aria-label="Photo of a frightened person"></div>
    <div class="pill pill--fears">FEARS</div>

    <div class="photo photo--frustrations" role="img" aria-label="Photo of a stressed person at a computer"></div>
    <div class="pill pill--frustrations">FRUSTRATIONS</div>

    <div class="photo photo--partners" role="img" aria-label="Photo of linked hands forming a circle"></div>
    <div class="pill pill--partners">PARTNERS</div>

    <svg class="clock" viewBox="0 0 56 56" aria-hidden="true">
      <circle cx="28" cy="28" r="26" fill="#ffffff" stroke="#333" stroke-width="2"/>
      <line x1="28" y1="28" x2="20" y2="22" stroke="#222" stroke-width="2" stroke-linecap="round"/>
      <line x1="28" y1="28" x2="38" y2="16" stroke="#222" stroke-width="1.5" stroke-linecap="round"/>
      <line x1="28" y1="28" x2="30" y2="44" stroke="#c0262d" stroke-width="1"/>
      <circle cx="28" cy="28" r="1.8" fill="#222"/>
    </svg>
    <div class="pill pill--time">TIME</div>
  </main>
</body>
</html>
```